First Aid Kit needs packaging design

We're looking for packaging design for our new first aid kit product. We have the logo created for the product. Our brand name is Bright Kestrel and our logo will be provided during the design process. We'll also provide photos (have high res files files for final design), and a template design to base off what we're looking for (packaging design template is .ai file). Logo file also attached (.psd & .png). We need to have the first aid kit contents listed on the back of the packaging (similar to the provided packaging template).

Color: We would like to see black, red, and white throughout the design (similar to provided design template)

The final design should communicate urgency, safety, and portability.

Final design should also include a FNSKU barcode (attached)

Below are more details that define the product.

Product Name:
Ultra-Portable & Small 100-Piece First Aid Kit w/ Exclusive Items, Light, Durable Nylon Case, Space Saving Design - A Must Have Survival Kit!

Product Attributes:
BASED ON CUSTOMER FEEDBACK, our newly designed ultra-lightweight and portable kit has been upgraded with BETTER and STRONGER emergency supplies. Stronger scissors and tweezers, more precise compass, sting relief pads, antibacterial ointment and more!
PRODUCED WITH THE HIGHEST QUALITY STANDARDS that only KLV Approved Facilities can meet.
LIGHTWEIGHT, DURABLE & COMPACT. Perfect for an emergency where a bright kestrel is necessary to because seconds count!
The ULTIMATE First Aid Kit for Camping, Home, Road Trips, Office, Adventure, School, Workplace, Travel or Sports.

Product Description
Learn How This Ultra-Portable, Light And Rugged First-Aid Kit Can Give You And Your Family The Ultimate Peace Of Mind.
You need to act fast! Quick Action And A Bright Kestrel Is Critical In Emergency Situations.

Stay Alert! Our Kit Has Been Redesigned And Bolstered Based On Your Feedback. Weighing Under 1lb. This Is The Lightest First Aid Kit In Its Class! If You Don't Know What To Do, No Problem; We've Included A First Aid Instruction Guide So You Can Administer Aid Correctly.

Take A Look Inside:

Antiseptic cleansing wipes (6 pcs)
Alcohol prep pad (10 pcs)
Butterfly closure strips (6 pcs)
Sterile Gauze Pad (3 pcs)
Extra large adhesive bandage (4 pc)
Adhesive bandages (25 pcs)
Antibacterial Ointment (4 pcs)
Knuckle adhesive bandage (3 pcs)
Fingertip adhesive bandage (3 pcs)
1 disposable cold compress
First aid tape (1 roll)
Cotton tip applicator (10 pcs)
Abdominal pad (1 pc)
Disposable vinyl gloves (2 pc)
Slim rescue howler whistle (1 pc)
Compass (1pc)
Moleskin blister relief (1 pc)
Triangular bandages (1 pc)
Disposable Emergency blanket (1 pc)
1 glow stick
Disposable raincoat (1 pc)
Scissors (1 pc)
PBT conforming bandage 5x3.6cm (1 roll)
CPR facemask (1 pc)
Metal tweezers (1 pc)
Razor Blade (1 pc)
Sewing Kit (1 pc)
Safety Pins (4 pc)
Sting Relief Pads (4 pc)

Let us know if there are any questions around this.

Thank you,

Owen

Target Market(s)

Health Care, First Aid, Sports & Outdoors, automotive safety, office safety

Industry/Entity Type

Health Care

Font styles to use
Sans Serif
Other font styles liked:
• similar to included box design frame/template

Colors
ec1f27
ffffff
000000

Requirements
Must have
• See Project Description
• Color: Black, red, and white
• Barcode: FNSKU Barcode attached
• Design on back needs to show included contents (similar to design template attached)
Nice to have
• See Project Description

```html
<!DOCTYPE html>
<html lang="en">
<head>
<meta charset="utf-8">
<title>Bright Kestrel First Aid Kit – Packaging</title>
<link rel="stylesheet" href="https://fonts.googleapis.com/css2?family=Exo+2:wght@500;600;700;800&display=swap">
<style>
  :root {
    --page-bg: #ffffff;
    --panel-light: #fbd9d5;
    --panel-mid: #f6bcb6;
    --panel-deep: #ef9d96;
    --brand-red: #e0211f;
    --deep-red: #8e1a1a;
    --icon-tint: #f3aaa3;
  }
  * { box-sizing: border-box; margin: 0; padding: 0; }
  html, body { width: 1200px; height: 536px; overflow: hidden; background: var(--page-bg); }
  body { position: relative; font-family: "Exo 2", sans-serif; }

  .panel {
    position: absolute;
    top: 112px;
    width: 450px;
    height: 304px;
    border-radius: 22px;
    overflow: hidden;
    background:
      radial-gradient(circle at 40% 35%, var(--panel-light) 0%, rgba(251,217,213,0) 60%),
      linear-gradient(160deg, var(--panel-light) 0%, var(--panel-mid) 55%, var(--panel-deep) 100%);
  }
  .panel--front { left: 110px; }
  .panel--back  { left: 692px; }

  .brand-mark {
    position: absolute;
    display: flex;
    align-items: center;
    color: var(--brand-red);
    font-weight: 800;
    white-space: nowrap;
  }
  .brand-mark__dot { border-radius: 50%; background: var(--brand-red); flex: none; }

  .panel--front .brand-mark { left: 50px; top: 98px; width: 320px; justify-content: center; gap: 10px; font-size: 24px; }
  .panel--front .brand-mark__dot { width: 26px; height: 26px; }

  .panel--back .brand-mark { left: 24px; top: 46px; width: 200px; justify-content: center; gap: 6px; font-size: 15px; }
  .panel--back .brand-mark__dot { width: 16px; height: 16px; }

  .product-title { position: absolute; text-align: center; font-weight: 700; }
  .product-title__tag { display: block; color: var(--deep-red); font-weight: 600; }
  .product-title__name { display: block; color: var(--brand-red); font-weight: 800; }
  .product-title__claim { display: block; color: var(--brand-red); font-weight: 700; }

  .panel--front .product-title { left: 60px; top: 205px; width: 300px; }
  .panel--front .product-title__tag { font-size: 11.5px; line-height: 14px; }
  .panel--front .product-title__name { font-size: 27px; line-height: 28px; }
  .panel--front .product-title__claim { font-size: 11.5px; line-height: 13px; }

  .panel--back .product-title { left: 24px; top: 108px; width: 200px; }
  .panel--back .product-title__tag { font-size: 7.5px; line-height: 9px; }
  .panel--back .product-title__name { font-size: 17px; line-height: 18px; }
  .panel--back .product-title__claim { font-size: 7.5px; line-height: 9px; }

  .contents-icons {
    position: absolute;
    left: 42px; top: 166px;
    width: 152px; height: 122px;
    border-radius: 4px;
    background: linear-gradient(180deg, var(--icon-tint), var(--panel-deep));
    border: 1.5px solid var(--brand-red);
  }

  .contents {
    position: absolute;
    left: 244px; top: 18px;
    width: 196px;
  }
  .contents__title {
    color: var(--brand-red);
    font-size: 15px;
    font-weight: 700;
    margin-bottom: 7px;
    text-align: center;
  }
  .contents__list {
    list-style: none;
    color: var(--brand-red);
    font-size: 7px;
    font-weight: 600;
    line-height: 8.6px;
  }
  .contents__item { display: flex; justify-content: space-between; }
</style>
</head>
<body>

  <section class="panel panel--front" aria-label="Front of pack">
    <div class="brand-mark"><span class="brand-mark__dot"></span><span>Bright Kestrel</span></div>
    <h1 class="product-title">
      <span class="product-title__tag">Ultra-Portable &amp; Small 100-Piece</span>
      <span class="product-title__name">First Aid Kit</span>
      <span class="product-title__claim">A Must Have Survival Kit!</span>
    </h1>
  </section>

  <section class="panel panel--back" aria-label="Back of pack">
    <div class="brand-mark"><span class="brand-mark__dot"></span><span>Bright Kestrel</span></div>
    <h2 class="product-title">
      <span class="product-title__tag">Ultra-Portable &amp; Small 100-Piece</span>
      <span class="product-title__name">First Aid Kit</span>
      <span class="product-title__claim">A Must Have Survival Kit!</span>
    </h2>

    <div class="contents-icons" role="img" aria-label="Grid of sixteen line icons showing kit items: whistle, gauze, blanket, compass, glow stick, facemask, gloves, raincoat, safety pin, razor blade, tweezers, tape roll, bandage, cotton swab, sewing needle and ointment"></div>

    <div class="contents">
      <h3 class="contents__title">Take A Look Inside</h3>
      <ul class="contents__list">
        <li class="contents__item"><span>Abdominal pad</span><span>1 pc</span></li>
        <li class="contents__item"><span>Adhesive bandages</span><span>25 pcs</span></li>
        <li class="contents__item"><span>Alcohol prep pad</span><span>10 pcs</span></li>
        <li class="contents__item"><span>Antibacterial Ointment</span><span>4 pcs</span></li>
        <li class="contents__item"><span>Antiseptic cleansing wipes</span><span>6 pcs</span></li>
        <li class="contents__item"><span>Butterfly closure strips</span><span>6 pcs</span></li>
        <li class="contents__item"><span>Compass</span><span>1 pc</span></li>
        <li class="contents__item"><span>Cotton tip applicator</span><span>10 pcs</span></li>
        <li class="contents__item"><span>CPR facemask</span><span>1 pc</span></li>
        <li class="contents__item"><span>Disposable cold compress</span><span>1 pc</span></li>
        <li class="contents__item"><span>Disposable Emergency blanket</span><span>1 pc</span></li>
        <li class="contents__item"><span>Disposable raincoat</span><span>1 pc</span></li>
        <li class="contents__item"><span>Disposable vinyl gloves</span><span>2 pc</span></li>
        <li class="contents__item"><span>Extra large adhesive bandage</span><span>4 pc</span></li>
        <li class="contents__item"><span>Fingertip adhesive bandage</span><span>3 pcs</span></li>
        <li class="contents__item"><span>First aid tape</span><span>1 roll</span></li>
        <li class="contents__item"><span>Glow stick</span><span>1 pc</span></li>
        <li class="contents__item"><span>Knuckle adhesive bandage</span><span>3 pcs</span></li>
        <li class="contents__item"><span>Metal tweezers</span><span>1 pc</span></li>
        <li class="contents__item"><span>Moleskin blister relief</span><span>1 pc</span></li>
        <li class="contents__item"><span>PBT conforming bandage 5x3.6cm</span><span>1 roll</span></li>
        <li class="contents__item"><span>Razor Blade</span><span>1 pc</span></li>
        <li class="contents__item"><span>Safety Pins</span><span>4 pc</span></li>
        <li class="contents__item"><span>Scissors</span><span>1 pc</span></li>
        <li class="contents__item"><span>Sewing Kit</span><span>1 pc</span></li>
        <li class="contents__item"><span>Slim rescue howler whistle</span><span>1 pc</span></li>
        <li class="contents__item"><span>Sterile Gauze Pad</span><span>3 pcs</span></li>
        <li class="contents__item"><span>Sting Relief Pads</span><span>4 pc</span></li>
        <li class="contents__item"><span>Triangular bandages</span><span>1 pc</span></li>
      </ul>
    </div>
  </section>

</body>
</html>
```